Glossaro: Graphic elements & webpage layout

Hi there! We’re building a site called Glossaro.com—it will be a community site for beauty product reviews, product recommendations and beauty tutorials. We've already got a logo, thanks to another ArtHively project. This project on ArtHively involves the following web design work:

1) Propose the overall graphic design elements of our site (according to our guidelines, which are in the attached file)

-Color Palette
-Fonts
-Icon set(s)

2) Using the overall graphic design elements in step 1 and our storyboard (attached), develop a webpage layout for the "How-to" page of our site. The "How-to" pages will be an editorial format, where our beauty journalist will show a video (and photos) of step-by-step beauty tutorials.

Please take a look at the attached files for a detailed brief and the logo! Thanks and we're looking forward to working with you!

Target Market(s)

Glossaro is for a French, English, and American audience of women between the ages of 16 and 30, who buy and use beauty products regularly.

Industry/Entity Type

Graphic Design

Requirements
Must have
• 1) A global set of graphic standards for the website Glossaro.com:
• A color palette
• Fonts
• An icon set (or sets)
• A menu
• Other graphic elements like button styles

2) A webpage layout (non-coded) for the How-To page template
(See storyboard, attached separately)
This webpage layout is for the main editorial format on Glossaro—step by step beauty tutorials. The individual on-page elements are in the storyboard, but overall we’d like it to look clean, friendly, and to encourage community participation and sharing on social networks.
Nice to have
• • A look and feel that is fresh, clean and modern
• Proximity: Establishes a close proximity with the user. (We want them to get the same feeling they get when talking beauty tips with their close friends).
• Neutrality: A sincere and neutral look and feel that doesn’t suggest a preference for any particular or elite type of beauty (but it can still be fun!)
• The graphic design is relevant to the beauty sector as a whole. (We could be talking about lipstick, a hairbrush or a man’s cologne)
• The graphic design alludes to the beauty industry (discreetly, not overtly!)
Should not have
• We've already got a logo, so you shouldn't suggest a new one!

We really want to avoid designs that are too traditionally "beauty" or too girly and feminine. Please no pink, no flowers, etc! :)

```html
<!DOCTYPE html>
<html lang="fr">
<head>
<meta charset="utf-8">
<title>Glossaro – How-to</title>
<link href="https://fonts.googleapis.com/css2?family=Open+Sans:wght@400;600;700&display=swap" rel="stylesheet">
<style>
:root{
  --teal:#1fbeb0;
  --teal-dark:#17a596;
  --ink:#1d1d1d;
  --muted:#777;
  --line:#b9b9b9;
  --white:#fff;
  --player:#2a2a2a;
  --controls:#cfcfcf;
}
*{box-sizing:border-box;margin:0;padding:0}
html,body{width:1200px;height:2252px;overflow:hidden}
body{position:relative;background:var(--white);font-family:"Open Sans",Arial,sans-serif;color:var(--ink)}
.abs{position:absolute}
.header{left:0;top:0;width:1200px;height:102px;background:var(--teal)}
.brand{left:51px;top:14px;color:var(--white);font-weight:700;font-size:50px;letter-spacing:-1px}
.langs{left:985px;top:22px;color:var(--white);font-weight:700;font-size:16px;word-spacing:8px}
.social{width:28px;height:28px;background:var(--white);border-radius:4px}
.social.small{width:26px;height:26px;background:var(--teal)}
.nav-btn{height:24px;background:#6dd8cf;color:var(--white);font-size:14px;font-weight:700;text-align:center;line-height:24px;border-radius:5px 5px 0 0}
.search-field{left:819px;top:57px;width:247px;height:24px;background:var(--white);border-radius:3px}
.search-btn{left:1072px;top:57px;width:74px;height:24px;background:#6dd8cf;color:var(--white);font-size:15px;font-weight:700;text-align:center;line-height:24px;border-radius:3px}
.title{left:51px;top:112px;font-size:26px}
.meta{left:51px;top:148px;font-size:16px;font-weight:600;display:flex;align-items:center;gap:8px}
.dot{width:26px;height:18px;border-radius:50%;background:var(--teal-dark)}
.dot.off{background:#d8f2ef}
.media{background:linear-gradient(135deg,#6a4a36,#b58a6a 55%,#7b5a44)}
.controls{height:24px;background:var(--controls)}
.controls svg{position:absolute;left:0;top:0}
.lede{width:597px;font-size:14.5px;line-height:19px}
.needs{left:722px;top:188px;width:424px;height:358px;background:var(--teal);border-radius:14px;color:var(--white);padding:22px 37px}
.needs h2{font-size:24px;font-weight:600;margin-bottom:18px}
.needs li{list-style:none;font-size:20px;font-weight:600;line-height:24px}
.needs li::before{content:"";display:inline-block;width:12px;height:12px;border-radius:50%;background:var(--white);margin-right:6px}
.step{left:51px;height:40px;background:var(--teal);color:var(--white);font-weight:700;font-size:24px;line-height:40px;padding-left:14px}
.tab{height:27px;font-size:15px;font-weight:700;line-height:25px;text-align:center;border-radius:6px 6px 0 0}
.tab.video{background:var(--white);color:var(--teal);border:2px solid var(--teal);border-bottom:none}
.tab.photos{background:var(--teal);color:var(--white)}
.shop{left:711px;width:435px;border:5px solid var(--teal);border-radius:16px;background:var(--white)}
.item{position:absolute;width:200px;height:85px}
.item .pic{position:absolute;left:0;top:0;width:118px;height:80px;background:linear-gradient(135deg,#c74b7e,#e7a9c0 50%,#8c2d55)}
.item .info{position:absolute;left:124px;top:0;color:var(--teal);font-size:14px;font-weight:600;line-height:17px}
.item .buy{display:block;margin-top:4px;width:60px;height:20px;background:var(--teal);color:var(--white);font-size:12px;line-height:20px;text-align:center;border-radius:2px}
.gallery{background:var(--player)}
.gallery .photo{position:absolute;left:68px;top:0;width:438px;height:362px;background:linear-gradient(150deg,#e8ddd2,#7a4a2c 60%,#3c2316)}
.arrow{position:absolute;width:46px;height:48px;background:var(--teal);border-radius:8px}
.comments-bar{left:51px;top:1758px;width:268px;height:45px;background:var(--teal);color:var(--white);font-weight:700;font-size:24px;line-height:45px;padding-left:12px}
.label{left:56px;font-size:14px;font-weight:700}
.field{border:2px solid var(--line);background:var(--white)}
.textarea{left:51px;top:1931px;width:597px;height:46px;padding:10px 12px;font-size:14px;font-weight:600}
.submit{left:546px;top:1985px;width:102px;height:28px;background:var(--teal);color:var(--white);font-size:14px;font-weight:600;line-height:28px;text-align:center;border-radius:14px}
.comment{left:51px;top:2028px;width:597px;height:114px;border:2px solid #888;padding:8px 12px;font-size:14px;font-weight:600;line-height:18px}
.footer{left:0;top:2167px;width:1200px;height:85px;background:var(--teal);color:var(--white);font-size:30px;font-weight:600;text-align:center;line-height:85px}
</style>
</head>
<body>
<header class="abs header">
  <div class="abs brand">Glossaro</div>
  <div class="abs langs">FR EN AM</div>
  <div class="abs social" style="left:1090px;top:16px"></div>
  <div class="abs social" style="left:1128px;top:16px"></div>
  <div class="abs nav-btn" style="left:632px;top:57px;width:85px">HOW TO</div>
  <div class="abs nav-btn" style="left:728px;top:57px;width:85px">TIPS</div>
  <div class="abs search-field"></div>
  <div class="abs search-btn">Search</div>
</header>

<h1 class="abs title">[TITRE DU TUTORIAL]</h1>
<div class="abs social small" style="left:589px;top:114px"></div>
<div class="abs social small" style="left:621px;top:114px"></div>
<div class="abs meta">Difficulté: <span class="dot"></span><span class="dot"></span><span class="dot off"></span> Durée: 20 minutes Occasion: Soirée</div>

<div class="abs media" role="img" aria-label="Vidéo du tutoriel : application de poudre au pinceau" style="left:51px;top:188px;width:597px;height:335px"></div>
<div class="abs controls" style="left:51px;top:523px;width:597px">
  <svg width="597" height="24"><path d="M18 6 L28 12 L18 18Z" fill="#333"/><rect x="40" y="10" width="140" height="4" fill="#333"/><rect x="186" y="10" width="330" height="4" fill="#333"/></svg>
</div>
<p class="abs lede" style="left:51px;top:563px">Lorem ipsum dolor sit amet, maiores ornare ac fermentum, imperdiet ut vivamus a, nam lectus at nunc. Quam euismod sem, semper ut potenti pellentesque quisque. In eget sapien sed, sit duis vestibulum ultricies, placerat morbi amet vel, nullam in in lorem vel.</p>

<aside class="abs needs">
  <h2>Les produits nécessaires</h2>
  <ul><li>Produit 1</li><li>Produit 2</li><li>Produit 3</li><li style="list-style:none">&nbsp;&nbsp;...</li></ul>
</aside>

<div class="abs step" style="top:671px;width:128px">ETAPE 1</div>
<div class="abs tab video" style="left:51px;top:722px;width:90px">Vidéo</div>
<div class="abs tab photos" style="left:145px;top:722px;width:97px">Photos</div>
<div class="abs media" role="img" aria-label="Vidéo de l'étape 1 : préparation de la peau" style="left:51px;top:751px;width:597px;height:330px;background:linear-gradient(135deg,#d9c7b8,#f1e4d9 50%,#c9b2a0)"></div>
<div class="abs controls" style="left:51px;top:1081px;width:597px">
  <svg width="597" height="24"><path d="M18 6 L28 12 L18 18Z" fill="#333"/><rect x="40" y="10" width="140" height="4" fill="#333"/><rect x="186" y="10" width="330" height="4" fill="#333"/></svg>
</div>
<p class="abs lede" style="left:51px;top:1123px">Lorem ipsum dolor sit amet, maiores ornare ac fermentum, imperdiet ut vivamus a, nam lectus at nunc. Quam euismod sem, semper ut potenti pellentesque quisque. In eget sapien sed, sit duis vestibulum ultricies, placerat morbi amet vel, nullam in in lorem vel.</p>

<section class="abs shop" style="top:748px;height:373px">
  <div class="item" style="left:18px;top:35px"><div class="pic" role="img" aria-label="Photo produit"></div><div class="info">Produit 1<br>Marque<br>Prix<span class="buy">Acheter</span></div></div>
  <div class="item" style="left:220px;top:35px"><div class="pic" role="img" aria-label="Photo produit"></div><div class="info">Produit 1<br>Marque<br>Prix<span class="buy">Acheter</span></div></div>
  <div class="item" style="left:18px;top:140px"><div class="pic" role="img" aria-label="Photo produit"></div><div class="info">Produit 1<br>Marque<br>Prix<span class="buy">Acheter</span></div></div>
  <div class="item" style="left:220px;top:140px"><div class="pic" role="img" aria-label="Photo produit"></div><div class="info">Produit 1<br>Marque<br>Prix<span class="buy">Acheter</span></div></div>
  <div class="item" style="left:18px;top:245px"><div class="pic" role="img" aria-label="Photo produit"></div><div class="info">Produit 1<br>Marque<br>Prix<span class="buy">Acheter</span></div></div>
  <div class="item" style="left:220px;top:245px"><div class="pic" role="img" aria-label="Photo produit"></div><div class="info">Produit 1<br>Marque<br>Prix<span class="buy">Acheter</span></div></div>
</section>

<div class="abs step" style="top:1217px;width:128px">ETAPE 2</div>
<div class="abs tab video" style="left:51px;top:1271px;width:90px">Vidéo</div>
<div class="abs tab photos" style="left:145px;top:1271px;width:97px">Photos</div>
<div class="abs gallery" style="left:51px;top:1302px;width:597px;height:362px">
  <div class="photo" role="img" aria-label="Photo de l'étape 2 : coiffure ondulée"></div>
  <div class="arrow" style="left:17px;top:168px"><svg width="46" height="48"><path d="M28 12 L16 24 L28 36" stroke="#fff" stroke-width="6" fill="none"/></svg></div>
  <div class="arrow" style="left:534px;top:168px"><svg width="46" height="48"><path d="M18 12 L30 24 L18 36" stroke="#fff" stroke-width="6" fill="none"/></svg></div>
</div>
<p class="abs lede" style="left:51px;top:1678px">Lorem ipsum dolor sit amet, maiores ornare ac fermentum, imperdiet ut vivamus a, nam lectus at nunc. Quam euismod sem, semper ut potenti pellentesque quisque. In eget sapien sed, sit duis vestibulum ultricies, placerat morbi amet vel, nullam in in lorem vel.</p>

<section class="abs shop" style="top:1300px;height:236px">
  <div class="item" style="left:18px;top:18px"><div class="pic" role="img" aria-label="Photo produit"></div><div class="info">Produit 1<br>Marque<br>Prix<span class="buy">Acheter</span></div></div>
  <div class="item" style="left:220px;top:18px"><div class="pic" role="img" aria-label="Photo produit"></div><div class="info">Produit 1<br>Marque<br>Prix<span class="buy">Acheter</span></div></div>
  <div class="item" style="left:18px;top:123px"><div class="pic" role="img" aria-label="Photo produit"></div><div class="info">Produit 1<br>Marque<br>Prix<span class="buy">Acheter</span></div></div>
  <div class="item" style="left:220px;top:123px"><div class="pic" role="img" aria-label="Photo produit"></div><div class="info">Produit 1<br>Marque<br>Prix<span class="buy">Acheter</span></div></div>
</section>

<div class="abs comments-bar">COMMENTARIES (12)</div>
<div class="abs label" style="top:1836px">Nom</div>
<div class="abs field" style="left:213px;top:1820px;width:435px;height:34px"></div>
<div class="abs label" style="top:1880px">Mail(n'apparaitra pas)</div>
<div class="abs field" style="left:213px;top:1871px;width:435px;height:37px"></div>
<div class="abs field textarea">Laissez votre commentaire ici !</div>
<div class="abs submit">Commenter</div>
<div class="abs comment">Lorem ipsum dolor sit amet, maiores ornare ac fermentum, imperdiet ut vivamus a, nam lectus at nunc. Quam euismod sem, semper ut potenti pellentesque quisque. In eget sapien sed, sit duis vestibulum ultricies, placerat morbi amet vel, nullam in in lorem vel.<br>Commentaire de [nom] posté le [date]</div>

<footer class="abs footer">Velune</footer>
</body>
</html>
```